Morning Harbor Community Chapel needs a new Business Card/Letterhead Suite

***** IT DOES NOT HAVE TO FEATURE GREEN AND BROWN in order to be a successful design*****

****FONTS: SF New Republic, 'Morning Harbor'; Nexa Light, 'Community Chapel'****

***We have two locations, with two addresses. So the business card AND letterhead need to include two sets of address information***

We are a growing church in New York in need of a new stationary suite. We have recently adopted a new logo (via a successful PixelGuild project) and need new business cards, letterhead, envelopes, and folders.

We would like to see creative, original designs that are modern and clean/elegant (NOT dated "churchy" graphics that are cheesy).

We need this project worked on immediately, as we need to print new business cards for upcoming programs we have on our schedule. So, the designs need to be solid so that we can move quickly throughout the revision process toward print.

We'd also need editables files, so that we can drop in other staff members names/phone numbers, to be able to print cards for those staff needing them.

Requirements
Must have
• Our logo
• Must be given to us in an editable format (to change names)
Nice to have
• Some examples on grey, or recycled, card stock
• card stock (background) does not have to be white
Should not have
• Any extraneous logo's or symbols

```html
<!DOCTYPE html>
<html lang="en">
<head>
<meta charset="utf-8">
<title>Morning Harbor Community Chapel – Stationery Suite</title>
<link href="https://fonts.googleapis.com/css2?family=Questrial&display=swap" rel="stylesheet">
<style>
  :root {
    --backdrop: #dedede;
    --paper: #ffffff;
    --paper-soft: #f4f4f3;
    --card-grey: #d3d3d2;
    --olive: #6c6a45;
    --brand-green: #4d7c34;
    --ink: #3a3a3a;
    --ink-soft: #6b6b6b;
    --leaf-tint: rgba(175, 195, 170, 0.35);
    --leaf-tint-dark: rgba(140, 140, 105, 0.55);
  }
  * { margin: 0; padding: 0; box-sizing: border-box; }
  html, body { width: 1200px; height: 410px; overflow: hidden; }
  body {
    background: var(--backdrop);
    font-family: "Questrial", "Century Gothic", sans-serif;
    color: var(--ink);
    position: relative;
  }
  .piece { position: absolute; box-shadow: 0 1px 3px rgba(0,0,0,0.18); overflow: hidden; }
  .wordmark { color: var(--brand-green); font-weight: 400; text-align: center; line-height: 1; }
  .wordmark .name { display: block; }
  .wordmark .sub { display: block; letter-spacing: 0.18em; text-transform: uppercase; }
  .foliage { position: absolute; }

  /* Business card back */
  .card-back { left: 26px; top: 33px; width: 152px; height: 88px; background: var(--card-grey); }
  .card-back .wordmark { position: absolute; right: 10px; top: 12px; text-align: right; }
  .card-back .wordmark .name { font-size: 8px; }
  .card-back .wordmark .sub { font-size: 3px; }
  .card-back .address { position: absolute; right: 10px; top: 31px; font-size: 3px; line-height: 1.35; text-align: right; color: var(--ink-soft); }
  .card-back .person { position: absolute; left: 10px; top: 55px; }
  .card-back .person-name { font-size: 4.5px; color: var(--brand-green); }
  .card-back .person-role { font-size: 3px; color: var(--ink-soft); letter-spacing: 0.05em; }
  .card-back .contact { position: absolute; right: 10px; top: 58px; font-size: 3px; line-height: 1.45; text-align: right; color: var(--ink-soft); }

  /* Business card front */
  .card-front { left: 158px; top: 88px; width: 154px; height: 90px; background: var(--card-grey); }
  .card-front .wordmark { position: absolute; left: 0; right: 0; top: 36px; }
  .card-front .wordmark .name { font-size: 13px; }
  .card-front .wordmark .sub { font-size: 4.5px; margin-top: 2px; }

  /* Envelope back */
  .envelope-back { left: 64px; top: 196px; width: 248px; height: 112px; background: var(--paper-soft); }
  .envelope-back .flap { position: absolute; left: 0; top: 0; width: 100%; height: 36px; background: var(--olive); }
  .envelope-back .wordmark { position: absolute; left: 0; right: 0; top: 16px; color: var(--paper); }
  .envelope-back .wordmark .name { font-size: 8px; }
  .envelope-back .wordmark .sub { font-size: 3px; }

  /* Envelope front */
  .envelope-front { left: 30px; top: 262px; width: 246px; height: 114px; background: var(--paper); }
  .envelope-front .wordmark { position: absolute; left: 12px; top: 20px; text-align: left; }
  .envelope-front .wordmark .name { font-size: 10px; }
  .envelope-front .wordmark .sub { font-size: 3.5px; margin-top: 1px; }
  .envelope-front .address { position: absolute; left: 12px; top: 46px; font-size: 3.5px; line-height: 1.35; color: var(--ink-soft); }

  /* Letterhead */
  .letterhead { left: 335px; top: 30px; width: 246px; height: 348px; background: var(--paper); }
  .letterhead .wordmark { position: absolute; left: 0; right: 0; top: 30px; }
  .letterhead .wordmark .name { font-size: 13px; }
  .letterhead .wordmark .sub { font-size: 4.5px; margin-top: 2px; }
  .letterhead .rule { position: absolute; left: 78px; width: 90px; top: 52px; height: 1px; background: #e2e2e2; }
  .letterhead .letter { position: absolute; left: 21px; top: 96px; width: 200px; }
  .letterhead .salutation { font-size: 5.5px; margin-bottom: 10px; }
  .letterhead .letter p { font-size: 3.4px; line-height: 1.5; color: var(--ink-soft); margin-bottom: 6px; }
  .letterhead .signature { width: 46px; height: 14px; margin-top: 4px; background: linear-gradient(90deg, rgba(60,60,60,0.15), rgba(60,60,60,0.05)); border-radius: 2px; }
  .letterhead .footer { position: absolute; left: 0; right: 0; top: 323px; text-align: center; font-size: 3px; line-height: 1.5; color: var(--ink-soft); }
  .letterhead .footer .mark { display: inline-block; width: 3px; height: 3px; border-radius: 50%; background: var(--brand-green); margin-right: 2px; vertical-align: middle; }

  /* Folders */
  .folder { top: 30px; width: 272px; height: 348px; }
  .folder .wordmark { position: absolute; left: 0; right: 0; top: 155px; }
  .folder .wordmark .name { font-size: 29px; }
  .folder .wordmark .sub { font-size: 9.5px; margin-top: 4px; }
  .folder .spine { position: absolute; top: 0; bottom: 0; width: 1px; }
  .folder-light { left: 604px; background: var(--paper-soft); }
  .folder-light .spine { background: #d8d8d8; }
  .folder-dark { left: 898px; background: var(--olive); }
  .folder-dark .spine { background: rgba(255,255,255,0.18); }
  .folder-dark .wordmark { color: var(--paper); }
</style>
</head>
<body>

  <section class="piece card-back" aria-label="Business card, contact side">
    <div class="foliage" role="img" aria-label="Faint leafy stem decoration" style="left:8px;top:18px;width:60px;height:70px;background:radial-gradient(ellipse at 40% 70%, var(--leaf-tint), transparent 70%);"></div>
    <div class="wordmark"><span class="name">Morning Harbor</span><span class="sub">Community Chapel</span></div>
    <div class="address">18 Beacon Road,<br>Larkfield, NY 11900<br><br>Offices:<br>4620 Beacon Road,<br>Larkfield, NY 11900</div>
    <div class="person"><div class="person-name">RAY HOLLOWAY, D.Min.</div><div class="person-role">SENIOR PASTOR</div></div>
    <div class="contact">555.204.7781<br>555.204.7790<br>pastor@mhchapel.org<br>www.mhchapel.org</div>
  </section>

  <section class="piece card-front" aria-label="Business card, name side">
    <div class="wordmark"><span class="name">Morning Harbor</span><span class="sub">Community Chapel</span></div>
  </section>

  <section class="piece envelope-back" aria-label="Envelope, flap side">
    <div class="flap"></div>
    <div class="wordmark"><span class="name">Morning Harbor</span><span class="sub">Community Chapel</span></div>
    <div class="foliage" role="img" aria-label="Faint leafy stem decoration" style="right:10px;top:40px;width:70px;height:70px;background:radial-gradient(ellipse at 60% 60%, var(--leaf-tint), transparent 70%);"></div>
  </section>

  <section class="piece envelope-front" aria-label="Envelope, address side">
    <div class="wordmark"><span class="name">Morning Harbor</span><span class="sub">Community Chapel</span></div>
    <div class="address">4620 Beacon Road,<br>Larkfield, NY 11900</div>
    <div class="foliage" role="img" aria-label="Faint leafy stem decoration" style="right:10px;top:10px;width:110px;height:104px;background:radial-gradient(ellipse at 60% 70%, var(--leaf-tint), transparent 70%);"></div>
  </section>

  <section class="piece letterhead" aria-label="Letterhead">
    <div class="wordmark"><span class="name">Morning Harbor</span><span class="sub">Community Chapel</span></div>
    <div class="rule"></div>
    <div class="foliage" role="img" aria-label="Faint leafy stem decoration" style="left:0;right:0;top:230px;height:118px;background:radial-gradient(ellipse at 75% 60%, var(--leaf-tint), transparent 70%);"></div>
    <div class="letter">
      <div class="salutation">Dear Mr. Delaney,</div>
      <p>We are grateful for your kind support this season. Our doors stay open to every neighbor who needs a place to rest, learn and grow together in faith.</p>
      <p>Our weekly programs continue to expand, and volunteers now serve meals, tutor children and visit homebound members across the town each week.</p>
      <p>This spring we will open a second ministry center, giving room for classes, counseling and youth gatherings throughout the year.</p>
      <p>Thank you for standing with us. We look forward to sharing more news soon.</p>
      <p>Sincerely,</p>
      <div class="signature" role="img" aria-label="Handwritten signature"></div>
    </div>
    <div class="footer">
      <div><span class="mark"></span>Main Campus: 18 Beacon Road, Larkfield, NY 11900</div>
      <div><span class="mark"></span>Ministry Center: 4620 Beacon Road, Larkfield, NY 11900</div>
      <div><span class="mark"></span>555.204.7781 <span class="mark"></span>www.mhchapel.org</div>
    </div>
  </section>

  <section class="piece folder folder-light" aria-label="Presentation folder, light">
    <div class="spine" style="left:6px"></div><div class="spine" style="left:10px"></div><div class="spine" style="left:14px"></div>
    <div class="foliage" role="img" aria-label="Faint leafy stem decoration" style="left:90px;right:0;top:130px;bottom:0;background:radial-gradient(ellipse at 65% 55%, var(--leaf-tint), transparent 70%);"></div>
    <div class="wordmark"><span class="name">Morning Harbor</span><span class="sub">Community Chapel</span></div>
  </section>

  <section class="piece folder folder-dark" aria-label="Presentation folder, olive">
    <div class="spine" style="left:4px"></div><div class="spine" style="left:8px"></div><div class="spine" style="left:12px"></div>
    <div class="foliage" role="img" aria-label="Faint leafy stem decoration" style="left:40px;right:0;top:130px;bottom:0;background:radial-gradient(ellipse at 75% 55%, var(--leaf-tint-dark), transparent 70%);"></div>
    <div class="wordmark"><span class="name">Morning Harbor</span><span class="sub">Community Chapel</span></div>
  </section>

</body>
</html>
```